Business Card Design

Two women who are flipping houses. Want the women with sledge hammers and in work boots. Liked the ones for cleaning with the woman but just needs some modifications to the women. On the back, I want both of our names and phone numbers.

Juliana Ashworth
555-218-4073

Beatrix Ashworth
555-307-9182

Business

WHAT COULD GO WRONG!!!!

```html
<!DOCTYPE html>
<html lang="en">
<head>
<meta charset="utf-8">
<title>What Could Go Wrong – Business Card</title>
<link rel="stylesheet" href="https://fonts.googleapis.com/css2?family=Allerta+Stencil&family=Special+Elite&display=swap">
<style>
  :root {
    --page-bg: #ecebe8;
    --board-dark: #1c1c1c;
    --board-mid: #2c2c2c;
    --chalk-soft: #b9b9b9;
    --chalk-bright: #f2f2f2;
    --card-white: #ffffff;
    --frame-black: #141414;
    --stencil-grey: #5e5e5e;
    --figure-tone-a: #c9ccd1;
    --figure-tone-b: #9aa0a8;
  }
  * { box-sizing: border-box; margin: 0; padding: 0; }
  html, body { width: 1200px; height: 784px; overflow: hidden; }
  body { background: var(--page-bg); position: relative; }

  .card {
    position: absolute;
    top: 237px;
    width: 540px;
    height: 309px;
    box-shadow: 0 6px 18px rgba(0,0,0,0.18);
  }

  /* Back: names and numbers on a chalkboard */
  .card-back {
    left: 30px;
    background: radial-gradient(ellipse at 45% 40%, var(--board-mid), var(--board-dark) 80%);
    display: flex;
    flex-direction: column;
    align-items: center;
    justify-content: center;
    gap: 26px;
    font-family: "Special Elite", "Courier New", monospace;
  }
  .contact { text-align: center; line-height: 1.25; }
  .contact-name { color: var(--chalk-soft); font-size: 24px; letter-spacing: 2px; }
  .contact-phone { color: var(--chalk-bright); font-size: 24px; letter-spacing: 2px; }

  /* Front: wordmark with two figures */
  .card-front {
    left: 630px;
    background: var(--card-white);
    padding: 10px;
  }
  .frame {
    position: relative;
    width: 100%;
    height: 100%;
    border: 7px solid var(--frame-black);
    outline: 2px solid var(--frame-black);
    outline-offset: -13px;
    overflow: hidden;
  }
  .wordmark {
    position: absolute;
    inset: 0;
    font-family: "Allerta Stencil", "Arial Black", sans-serif;
    font-weight: 400;
    color: var(--stencil-grey);
    line-height: 0.9;
  }
  .wordmark-line { position: absolute; white-space: nowrap; letter-spacing: -1px; }
  .line-one { left: 24px; top: 26px; font-size: 84px; }
  .line-two { left: 128px; top: 112px; font-size: 72px; }
  .line-three { left: 122px; top: 192px; font-size: 58px; }

  .figure {
    position: absolute;
    border-radius: 40px 40px 6px 6px;
    background: linear-gradient(180deg, var(--figure-tone-a), var(--figure-tone-b));
  }
  .figure-left { left: 18px; top: 108px; width: 92px; height: 160px; }
  .figure-right { right: 20px; top: 14px; width: 74px; height: 140px; }
</style>
</head>
<body>
  <section class="card card-back" aria-label="Card back">
    <div class="contact">
      <p class="contact-name">Juliana Ashworth</p>
      <p class="contact-phone">555-218-4073</p>
    </div>
    <div class="contact">
      <p class="contact-name">Beatrix Ashworth</p>
      <p class="contact-phone">555-307-9182</p>
    </div>
  </section>

  <section class="card card-front" aria-label="Card front">
    <div class="frame">
      <div class="figure figure-right" role="img" aria-label="Illustration of a woman in a cap and plaid shirt leaning on a sledgehammer"></div>
      <h1 class="wordmark">
        <span class="wordmark-line line-one">WHAT</span>
        <span class="wordmark-line line-two">COULD</span>
        <span class="wordmark-line line-three">GO WRONG</span>
      </h1>
      <div class="figure figure-left" role="img" aria-label="Illustration of a woman in a hard hat and overalls holding a sledgehammer, wearing work boots"></div>
    </div>
  </section>
</body>
</html>
```